Clean professional design needed for landscape property business

We need a logo for a new lawncare, landscaping , property maintenance business called Meadow Trim.
Our services include lawn mowing, garden maintenance, clean ups and some property maintenance.
We want a double sided business card that is clean and very professional using the colour scheme from our logo which is provided.
the business card should have impact as we will use these to drop into people's letterboxes as a marketing drop.
Initially we want to see what you come up with so there is a very wide scope here to work with.
Updates

Project Deadline Extended
Reason: we feel our original deadline was too short. we have extended to give more time for quality submissions.

Target Market(s)

High end property owners who don't wish to do there own gardneing or property maintenance

Industry/Entity Type

Business

Contact Information for Business Card

Name
Postion/ Title
Phone number
mobile
web address
physical address

services offered

Font styles to use
Sans Serif

Requirements
Must have
• curved edges preferrred
Nice to have
• We like the idea of the logo being embossed or etched into the card so it looks like it is below the surface of the card
Should not have
• No stock images or characters.

```html
<!DOCTYPE html>
<html lang="en">
<head>
<meta charset="utf-8">
<title>Meadow Trim – Business Card</title>
<link rel="stylesheet" href="https://fonts.googleapis.com/css2?family=Josefin+Sans:wght@400;600;700&display=swap">
<style>
  :root {
    --page: #ecebe8;
    --card-white: #ffffff;
    --charcoal: #4a4a4a;
    --charcoal-light: #5e5e5e;
    --ink: #333333;
    --green: #79ad1a;
    --green-dark: #5c8a12;
    --text-light: #ffffff;
  }
  * { box-sizing: border-box; margin: 0; padding: 0; }
  html, body {
    width: 1200px;
    height: 720px;
    overflow: hidden;
    background: var(--page);
    font-family: "Josefin Sans", sans-serif;
  }
  .canvas {
    position: relative;
    width: 1200px;
    height: 720px;
  }
  .card {
    position: absolute;
    width: 560px;
    height: 334px;
    border-radius: 6px;
    overflow: hidden;
    box-shadow: 0 8px 24px rgba(0, 0, 0, 0.18);
  }

  /* Front */
  .card-front {
    left: 40px;
    top: 70px;
    background: var(--card-white);
  }
  .front-brand {
    position: absolute;
    left: 60px;
    top: 128px;
    display: flex;
    align-items: center;
    gap: 24px;
  }
  .front-brand .brand-name {
    font-size: 60px;
    font-weight: 700;
    color: var(--ink);
    letter-spacing: -1px;
    line-height: 1;
  }
  .front-brand .brand-square {
    width: 34px;
    height: 34px;
    background: var(--green);
  }

  /* Back */
  .card-back {
    left: 620px;
    top: 316px;
    background: var(--charcoal);
  }
  .back-shapes {
    position: absolute;
    inset: 0;
  }
  .holder {
    position: absolute;
    left: 300px;
    top: 22px;
    width: 200px;
    text-align: center;
    color: var(--text-light);
  }
  .holder-name {
    font-size: 30px;
    font-weight: 600;
    letter-spacing: 3px;
    line-height: 1;
  }
  .holder-title {
    margin-top: 6px;
    font-size: 19px;
    font-weight: 400;
  }
  .contact-list {
    position: absolute;
    left: 35px;
    top: 98px;
    list-style: none;
  }
  .contact-item {
    display: flex;
    align-items: center;
    gap: 9px;
    height: 32px;
    margin-bottom: 11px;
    color: var(--text-light);
    font-size: 15px;
    letter-spacing: 0.4px;
  }
  .contact-icon {
    width: 32px;
    height: 32px;
    flex: none;
  }
  .back-brand {
    position: absolute;
    left: 306px;
    top: 176px;
    display: flex;
    align-items: center;
    gap: 10px;
  }
  .back-brand .brand-name {
    font-size: 28px;
    font-weight: 700;
    color: var(--ink);
    letter-spacing: -0.5px;
    line-height: 1;
  }
  .back-brand .brand-square {
    width: 14px;
    height: 14px;
    background: var(--green);
  }
  .services {
    position: absolute;
    right: 42px;
    bottom: 14px;
    color: var(--text-light);
    font-size: 19px;
    letter-spacing: 0.3px;
  }
</style>
</head>
<body>
<main class="canvas">

  <section class="card card-front" aria-label="Business card front">
    <div class="front-brand">
      <span class="brand-name">Meadow Trim</span>
      <span class="brand-square"></span>
    </div>
  </section>

  <section class="card card-back" aria-label="Business card back">
    <svg class="back-shapes" viewBox="0 0 560 334" width="560" height="334" aria-hidden="true">
      <defs>
        <radialGradient id="charcoal-glow" cx="0.3" cy="0.45" r="0.6">
          <stop offset="0" stop-color="#5e5e5e"/>
          <stop offset="1" stop-color="#474747"/>
        </radialGradient>
      </defs>
      <rect width="560" height="334" fill="url(#charcoal-glow)"/>
      <!-- white panel -->
      <path d="M288 96 C 300 170, 290 260, 250 334 L 560 334 L 560 96 Z" fill="#ffffff"/>
      <!-- top band with darker edge -->
      <path d="M118 0 C 170 60, 300 100, 560 106 L 560 0 Z" fill="#5c8a12"/>
      <path d="M118 0 C 170 55, 300 92, 560 97 L 560 0 Z" fill="#79ad1a"/>
      <!-- bottom band with darker edge -->
      <path d="M252 334 C 300 290, 420 270, 560 272 L 560 334 Z" fill="#5c8a12"/>
      <path d="M262 334 C 310 296, 420 278, 560 279 L 560 334 Z" fill="#79ad1a"/>
    </svg>

    <div class="holder">
      <p class="holder-name">NAME</p>
      <p class="holder-title">Postion/ Title</p>
    </div>

    <ul class="contact-list">
      <li class="contact-item">
        <svg class="contact-icon" viewBox="0 0 32 32" aria-hidden="true">
          <circle cx="16" cy="16" r="14.5" fill="#4a4a4a" stroke="#79ad1a" stroke-width="2.5"/>
          <circle cx="16" cy="16" r="11" fill="#ffffff"/>
          <path d="M9.5 14 C 10 10.5, 22 10.5, 22.5 14 L 20 15 L 19 13 L 13 13 L 12 15 Z" fill="#4a4a4a"/>
          <path d="M11 21.5 L 12.5 16 L 19.5 16 L 21 21.5 Z" fill="#4a4a4a"/>
          <circle cx="16" cy="18.5" r="1.6" fill="#ffffff"/>
        </svg>
        Phone number
      </li>
      <li class="contact-item">
        <svg class="contact-icon" viewBox="0 0 32 32" aria-hidden="true">
          <circle cx="16" cy="16" r="14.5" fill="#4a4a4a" stroke="#79ad1a" stroke-width="2.5"/>
          <circle cx="16" cy="16" r="11" fill="#ffffff"/>
          <rect x="12" y="8.5" width="8" height="15" rx="1.5" fill="none" stroke="#4a4a4a" stroke-width="1.5"/>
          <line x1="12" y1="20.5" x2="20" y2="20.5" stroke="#4a4a4a" stroke-width="1.2"/>
        </svg>
        mobile
      </li>
      <li class="contact-item">
        <svg class="contact-icon" viewBox="0 0 32 32" aria-hidden="true">
          <circle cx="16" cy="16" r="14.5" fill="#4a4a4a" stroke="#79ad1a" stroke-width="2.5"/>
          <circle cx="16" cy="16" r="11" fill="#ffffff"/>
          <g fill="none" stroke="#4a4a4a" stroke-width="1.2">
            <circle cx="16" cy="16" r="7.5"/>
            <ellipse cx="16" cy="16" rx="3.5" ry="7.5"/>
            <line x1="8.5" y1="16" x2="23.5" y2="16"/>
            <line x1="9.5" y1="12" x2="22.5" y2="12"/>
            <line x1="9.5" y1="20" x2="22.5" y2="20"/>
          </g>
        </svg>
        web address
      </li>
      <li class="contact-item">
        <svg class="contact-icon" viewBox="0 0 32 32" aria-hidden="true">
          <circle cx="16" cy="16" r="14.5" fill="#4a4a4a" stroke="#79ad1a" stroke-width="2.5"/>
          <circle cx="16" cy="16" r="11" fill="#ffffff"/>
          <path d="M9.5 16 L 16 9.5 L 22.5 16 M 11.5 14.5 L 11.5 22.5 L 20.5 22.5 L 20.5 14.5 M 14.5 22.5 L 14.5 17.5 L 17.5 17.5 L 17.5 22.5" fill="none" stroke="#4a4a4a" stroke-width="1.5" stroke-linejoin="round"/>
        </svg>
        physical address
      </li>
    </ul>

    <div class="back-brand">
      <span class="brand-name">Meadow Trim</span>
      <span class="brand-square"></span>
    </div>

    <p class="services">services offered</p>
  </section>

</main>
</body>
</html>
```